Auto glass company

BRIGHTWAY
Roving Auto Glass, LLC
555-604-1937

* Windshield Replacement
* Rock Chip Repair
Danny "K"
Brightwayrovingautoglass@example.com
* Fully Insured

This is what I would like on the card. The image is what I had before. Looking for a logo possible too, couldn’t find a place to add that on. It’s a auto glass company.

Target Market(s)

Auto glass

Industry/Entity Type

Auto glass

Contact Information for Business Card

Logo, business name, phone number, windshield replacement, rock chip repair, insured, owner name Danny K, email address brightwayrovingautoglass@example.com

Colors

Designer to choose colors to be used in the design.

Requirements
Must have
• Logo, business name, phone number, windshield replacement, rock chip repair, insured, owner name Danny K, email address brightwayrovingautoglass@example.com

```html
<!DOCTYPE html>
<html lang="en">
<head>
<meta charset="UTF-8">
<title>Brightway Roving Auto Glass — Business Card</title>
<link rel="stylesheet" href="https://fonts.googleapis.com/css2?family=Anton&family=Roboto+Condensed:wght@700&display=swap">
<style>
  :root {
    --page-bg: #121214;
    --ink-white: #ffffff;
    --ink-silver: #e4e6e9;
    --ink-grey: #b9bcc0;
    --ink-dark: #141416;
    --panel-dark: rgba(8, 8, 10, 0.82);
    --band-dark: #1c1e22;
    --band-dark-2: #34373c;
  }
  * { margin: 0; padding: 0; box-sizing: border-box; }
  html, body { width: 900px; height: 1200px; overflow: hidden; }
  body { background: var(--page-bg); position: relative; }

  .business-card {
    position: absolute;
    left: 30px; top: 361px;
    width: 840px; height: 477px;
    overflow: hidden;
    background: var(--band-dark);
  }
  .interior-photo {
    position: absolute; inset: 0;
    background: linear-gradient(180deg,
      #4a4542 0%, #6b625c 9%, #c98b92 15%, #ef9f7a 22%,
      #3b4a7e 30%, #d46a3c 33%, #2e4f86 37%,
      #3d3c3e 44%, #2a2a2d 60%, #19191b 100%);
  }
  .title-panel {
    position: absolute;
    left: 68px; top: 204px;
    width: 296px; height: 199px;
    background: var(--panel-dark);
  }
  .company-name {
    position: absolute;
    left: 73px; top: 208px;
    font-family: "Anton", sans-serif;
    font-size: 66px; line-height: 1;
    color: var(--ink-silver);
    letter-spacing: -0.5px;
    white-space: nowrap;
  }
  .company-sub {
    position: absolute;
    left: 74px; top: 281px;
    font-family: "Anton", sans-serif;
    font-size: 30px; line-height: 1;
    color: var(--ink-grey);
    letter-spacing: -0.3px;
    white-space: nowrap;
  }
  .phone {
    position: absolute;
    left: 73px; top: 330px;
    font-family: "Anton", sans-serif;
    font-size: 54px; line-height: 1;
    color: var(--ink-white);
    letter-spacing: -0.5px;
    white-space: nowrap;
  }
  .services {
    position: absolute;
    left: 522px; top: 283px;
    list-style: none;
    font-family: "Anton", sans-serif;
    font-size: 26px; line-height: 36px;
    color: var(--ink-white);
    letter-spacing: -0.3px;
    white-space: nowrap;
  }
  .services li::before { content: "· "; }

  .contact-band {
    position: absolute;
    left: 0; top: 403px;
    width: 840px; height: 74px;
    background: linear-gradient(90deg, var(--band-dark) 40%, var(--band-dark-2) 100%);
  }
  .owner-plate {
    position: absolute; left: 0; top: 0;
    width: 274px; height: 74px;
  }
  .owner-name {
    position: absolute;
    left: 77px; top: 16px;
    font-family: "Roboto Condensed", sans-serif;
    font-weight: 700; font-size: 30px; line-height: 1.2;
    color: var(--ink-dark);
  }
  .email {
    position: absolute;
    left: 277px; top: 18px;
    display: flex; align-items: center; gap: 8px;
    font-family: "Roboto Condensed", sans-serif;
    font-weight: 700; font-size: 26px; line-height: 1.2;
    color: var(--ink-white);
    white-space: nowrap;
  }
  .email svg { flex: none; }
</style>
</head>
<body>
  <section class="business-card">
    <div class="interior-photo" role="img" aria-label="Photo from a car's driver seat looking through the windshield at a lit bridge and city skyline at sunset"></div>

    <div class="title-panel"></div>
    <div class="company-name">BRIGHTWAY</div>
    <div class="company-sub">ROVING AUTO GLASS, LLC</div>
    <div class="phone">555-604-1937</div>

    <ul class="services">
      <li>WINDSHIELD REPLACEMENT</li>
      <li>ROCK CHIP REPAIR</li>
      <li>FULLY INSURED</li>
    </ul>

    <div class="contact-band">
      <svg class="owner-plate" viewBox="0 0 274 74" aria-hidden="true">
        <defs>
          <linearGradient id="silverPlate" x1="0" y1="0" x2="1" y2="0.4">
            <stop offset="0" stop-color="#9ea2a7"/>
            <stop offset="0.35" stop-color="#f4f5f6"/>
            <stop offset="0.7" stop-color="#b8bbbf"/>
            <stop offset="1" stop-color="#e2e4e6"/>
          </linearGradient>
        </defs>
        <polygon points="0,0 229,0 274,74 0,74" fill="url(#silverPlate)"/>
      </svg>
      <div class="owner-name">Danny "K"</div>
      <div class="email">
        <svg width="24" height="18" viewBox="0 0 24 18" aria-hidden="true">
          <rect x="1" y="1" width="22" height="16" fill="none" stroke="#ffffff" stroke-width="2"/>
          <polyline points="1,1 12,10 23,1" fill="none" stroke="#ffffff" stroke-width="2"/>
          <line x1="1" y1="17" x2="9" y2="8" stroke="#ffffff" stroke-width="2"/>
          <line x1="23" y1="17" x2="15" y2="8" stroke="#ffffff" stroke-width="2"/>
        </svg>
        <span>Brightwayrovingautoglass@example.com</span>
      </div>
    </div>
  </section>
</body>
</html>
```